Website Redesign Project

Bright Harbour Consulting provides project management and project controls consultancy services to companies in many industry sectors, within Australia and overseas. My company has been developing a business brand through forging strong business relationships within industry. We provide innovative tools, concepts and solutions to management teams to assist them in better plan and managing there project portfolios.
SECTORS OF INDUSTRY WE SERVICE
★Oil & Gas
★Minerals & Metals
★Petrochemical
★Manufacturing
★Building & Construction
★Telecommunications
★Rail
★Civil
OLD WEBSITE
My old website www.brightharbourconsulting.com.au needs a complete overhaul in terms of how the web pages look and feel. I am trying to get away from the grey, washed out look as it is uninviting and dull. My clients commented that my webpage does not reflect who I am as a company or my core values. Think total redesign
DESIGN
I would like a webpage design that is modern and has a corporate image. It must be elegant, classy, and have an overall glossy appearance. I want something exciting that creates some excellent feedback from clients. It needs to have a savvy appearance and an attitude of a market leader. A generic website template cannot be used as I provide a unique service to clients. I do not need a website design that looks like my compeditors, I want something that stands out in the crowd and effectivly markets my bussinesses brand. I want my website to represent quality, so only high resolution images that are clear, sharp and in focus can be used. With this design, throw your standard webpage design concepts out the window, as I want something fresh, innovative, exciting and inviting. The overall design should appear uncluttered as all content needs to be there for a reason, so think functional.
It must be professional and of the highest calibre as my clients expect nothing less. I provide clients with innovative tools, concepts and solutions, so the design needs to be edgy and creative to align with my company’s core business services. The new design must promote the company’s brand and us as a market leader. It must communicate that we service many industry sectors and reflect our company’s creativity, vision, energy and drive.
WEBPAGE WRITTEN CONTENT
I am happy with the written content on each page within my old website. You may arrange the text how you see fit within the new design. On the main page of my old website the text is under scored, I am not a big fan of this. I currently do not like the format the text is in, I am looking for a formatt that is easy to read, looks flattering and pleasing to the eye.
MAIN PAGE DESIGN
The main page design needs to focus on my company as a brand, it must promote that I service many industry sectors. My old webpage had me pigeon holed as only providing services to oil and gas. This is incorrect as I service oil & gas, metals and minerals, Petrochemical, Manufacturing, Building & Construction, Telecommunications, Rail and civil.
WEBPAGE COLUR PREFERENCE
Prefer a white background with plenty of colour
TESTIMONIAL TAB
The testimonial tab on the task bar can be removed as it is no longer required.
FINISHED PRODUCT
The finished product will be uploaded by you to a nominated web hosting account. I will need a copy of all files associated with the design. A copy of the finished product will also be provided in formats that can me imported to Xara Pro Designer as I will update my website in 6 months or so using this tool.
Updates
I have updated the design brief after recieving feedback from several designers
Thanks
Hi All
I have just launched another project called "bright harbour consulting business card redesign project", you are all welcome to join this project.
Thanks
Target Market(s)
★Oil and Gas
★Mining and Resources
★Building and infrastructure
★Petrochemical
★Civil and roads
★Rail
Industry/Entity Type
Industry
Requirements
Must have
- ★Draw you in
★Hold your attention
★Identify company brand
★Highlight skills experience and expertise
★Be a unique design not generic
Should not have
- ★The webpage design should not be old fashioned
★ The design should not be based off a generic design template
★The webpage should not be cluttered; everything needs to be there for a reason.

```html
<!DOCTYPE html>
<html lang="en">
<head>
<meta charset="utf-8">
<title>Bright Harbour Consulting – Expertise</title>
<link rel="stylesheet" href="https://fonts.googleapis.com/css2?family=Open+Sans:wdth,wght@75,300;75,400;100,400&display=swap">
<style>
  :root {
    --band-top-1: #6f0b10;
    --band-top-2: #5c080c;
    --page-red: #be141b;
    --band-bottom-1: #4f070a;
    --band-bottom-2: #3c0508;
    --band-bottom-3: #240304;
    --nav-grey: #8e8080;
    --white: #ffffff;
    --pale: #f8eeee;
    --ink-red: #a50e15;
    --title-red: #8c0c12;
    --active-red: #e31b23;
    --rule: #2a0a0a;
  }
  * { box-sizing: border-box; margin: 0; padding: 0; }
  html, body { width: 1200px; height: 649px; overflow: hidden; }
  body {
    position: relative;
    background: var(--page-red);
    font-family: "Open Sans", "Arial Narrow", sans-serif;
    font-stretch: 75%;
  }
  .band { position: absolute; left: 0; width: 1200px; }
  .band-top-1 { top: 0; height: 36px; background: var(--band-top-1); }
  .band-top-2 { top: 36px; height: 34px; background: var(--band-top-2); }
  .band-bottom-1 { top: 548px; height: 33px; background: var(--band-bottom-1); }
  .band-bottom-2 { top: 581px; height: 34px; background: var(--band-bottom-2); }
  .band-bottom-3 { top: 615px; height: 34px; background: var(--band-bottom-3); }

  .nav-link {
    position: absolute; left: 23px;
    font-weight: 300;
    font-size: 48px; line-height: 1;
    color: var(--nav-grey);
    text-decoration: none;
    letter-spacing: -0.5px;
    white-space: nowrap;
  }
  .nav-about { top: -5px; }
  .nav-services { top: 29px; }
  .nav-knowledge { top: 543px; }
  .nav-experience { top: 577px; }
  .nav-projects { top: 611px; }

  .brand {
    position: absolute; top: 8px; right: 6px;
    display: flex; align-items: center; gap: 8px;
  }
  .brand-mark {
    width: 40px; height: 40px; border-radius: 50%;
    background: var(--active-red);
  }
  .brand-text { display: flex; flex-direction: column; }
  .brand-name {
    font-size: 22px; font-weight: 400; color: var(--white); line-height: 1.05;
    white-space: nowrap;
  }
  .brand-tagline {
    font-size: 9px; color: var(--white); opacity: .8; margin-top: 3px;
    white-space: nowrap;
  }

  .page-title {
    position: absolute; left: 24px; top: 101px;
    font-weight: 300;
    font-size: 46px; color: var(--white); line-height: 1;
    white-space: nowrap;
  }

  .hero-frame {
    position: absolute; left: 51px; top: 181px;
    width: 397px; height: 267px;
    border: 6px solid var(--white);
    background: linear-gradient(170deg, #4f82c4 0%, #86aedc 45%, #c9dcee 75%, #9aa9b6 100%);
  }

  .expertise-menu {
    position: absolute; left: 600px; top: 181px; width: 164px;
    list-style: none;
    border: 1px solid var(--rule);
  }
  .expertise-menu li {
    height: 24.3px; padding: 5px 4px 0;
    background: var(--pale);
    color: var(--ink-red);
    font-size: 12.5px; line-height: 1.2;
    border-top: 1px solid var(--rule);
    white-space: nowrap; overflow: hidden;
  }
  .expertise-menu li:first-child { border-top: none; }
  .expertise-menu li.is-active {
    height: 41px; padding-top: 4px;
    white-space: normal;
    background: var(--active-red); color: var(--white);
  }

  .detail-panel {
    position: absolute; left: 763px; top: 181px;
    width: 345px; height: 232px;
    background: var(--pale);
    border: 1px solid var(--rule);
    padding: 7px 5px;
    overflow: hidden;
  }
  .detail-title {
    font-weight: 400; font-size: 24px;
    color: var(--title-red); line-height: 1.2;
    white-space: nowrap;
  }
  .detail-list {
    list-style: circle; margin: 9px 0 0 32px;
    color: var(--title-red);
    font-size: 18.5px; line-height: 26px;
  }
  .detail-list li { padding-left: 4px; white-space: nowrap; }
</style>
</head>
<body>
  <div class="band band-top-1"></div>
  <div class="band band-top-2"></div>
  <div class="band band-bottom-1"></div>
  <div class="band band-bottom-2"></div>
  <div class="band band-bottom-3"></div>

  <a class="nav-link nav-about" href="#">ABOUT US</a>
  <a class="nav-link nav-services" href="#">SERVICES</a>

  <div class="brand">
    <span class="brand-mark"></span>
    <div class="brand-text">
      <span class="brand-name">Bright Harbour Consulting</span>
      <span class="brand-tagline">Providing Effective Project Controls and Management Solutions</span>
    </div>
  </div>

  <h1 class="page-title">EXPERTISE</h1>

  <div class="hero-frame" role="img" aria-label="Cable-stayed bridge under construction with a tower crane against a blue sky"></div>

  <ul class="expertise-menu">
    <li>Project Management</li>
    <li>Project Controls</li>
    <li>Process Making Approvals</li>
    <li>Solid Foundations Through</li>
    <li class="is-active">Systems Design and Implementation</li>
    <li>Develop | Design | Implement</li>
    <li>Resources</li>
    <li>Software</li>
    <li>History With</li>
    <li>Assisting Clients</li>
  </ul>

  <section class="detail-panel">
    <h2 class="detail-title">Systems Design and Implementation</h2>
    <ul class="detail-list">
      <li>Project control</li>
      <li>Project management</li>
      <li>Quality management</li>
      <li>Construction management</li>
      <li>Equipment and procurement</li>
      <li>Accommodation and resourcing</li>
      <li>Software selection &amp; integration</li>
    </ul>
  </section>

  <a class="nav-link nav-knowledge" href="#">KNOWLEDGE</a>
  <a class="nav-link nav-experience" href="#">EXPERIENCE</a>
  <a class="nav-link nav-projects" href="#">PROJECTS</a>
</body>
</html>
```